Women's Health Company needs business card

We need a business card for a USA based women's health care company. We use digital technology to enhance therapy prescribed by clinicians for their patients

```html
<!DOCTYPE html>
<html lang="en">
<head>
<meta charset="utf-8">
<title>Velora Health – Business Card</title>
<link href="https://fonts.googleapis.com/css2?family=Lato:wght@300;400;700&display=swap" rel="stylesheet">
<style>
  :root {
    --stage: #8f8f8f;
    --card: #ffffff;
    --teal: #74c0bb;
    --teal-soft: rgba(116, 192, 187, 0.45);
    --teal-clear: rgba(116, 192, 187, 0);
    --purple: #8e549e;
    --ink: #555555;
    --reverse: #ffffff;
  }
  * { margin: 0; padding: 0; box-sizing: border-box; }
  html, body {
    width: 1047px; height: 1200px; overflow: hidden;
    background: var(--stage);
    font-family: "Lato", sans-serif;
  }
  .canvas { position: relative; width: 1047px; height: 1200px; }
  .card {
    position: absolute; left: 160px; width: 741px; height: 424px;
    border-radius: 28px; overflow: hidden;
    box-shadow: 0 3px 6px rgba(0,0,0,0.25);
  }
  .card--front { top: 120px; background: var(--card); }
  .card--back { top: 634px; background: var(--purple); }

  .accent-field {
    position: absolute; left: 0; top: 0; bottom: 0; width: 260px;
    background: linear-gradient(100deg, var(--teal-soft) 0%, var(--teal-clear) 100%);
  }
  .accent-band {
    position: absolute; left: 0; top: 0; bottom: 0; width: 14px;
    background: var(--teal);
  }
  .accent-tab {
    position: absolute; top: 58px; right: 0;
    width: 12px; height: 65px; border-radius: 6px 0 0 6px;
    background: var(--purple);
  }
  .identity { position: absolute; right: 62px; top: 57px; text-align: right; }
  .identity__name {
    font-weight: 700; font-size: 45px; letter-spacing: 1px;
    color: var(--teal); line-height: 1;
  }
  .identity__role {
    font-weight: 400; font-size: 22px; color: var(--purple);
    margin-top: 4px; letter-spacing: 0.5px; line-height: 1.2;
  }
  .contacts {
    position: absolute; right: 64px; top: 154px;
    list-style: none; text-align: right;
    font-size: 20.5px; color: var(--ink); letter-spacing: 1px;
  }
  .contacts__item {
    display: flex; justify-content: flex-end; align-items: flex-start;
    line-height: 27px; margin-bottom: 3.5px;
  }
  .contacts__item--address { margin-bottom: 9px; }
  .contacts__icon { width: 16px; height: 16px; margin-left: 13px; margin-top: 6px; flex: none; }
  .contacts__icon path, .contacts__icon circle { fill: var(--purple); }

  .brand {
    position: absolute; left: 0; right: 0; top: 0; bottom: 0;
    display: flex; align-items: center; justify-content: center; gap: 18px;
  }
  .brand__mark { width: 22px; height: 22px; border-radius: 50%; background: var(--reverse); }
  .brand__name {
    font-weight: 300; font-size: 72px; letter-spacing: 4px;
    color: var(--reverse);
  }
</style>
</head>
<body>
<main class="canvas">
  <section class="card card--front" aria-label="Business card front">
    <div class="accent-field" role="img" aria-label="Brand accent artwork area">
      <span class="accent-band"></span>
    </div>
    <span class="accent-tab"></span>
    <div class="identity">
      <h1 class="identity__name">LAURA BENSON</h1>
      <p class="identity__role">Founder &amp; CEO</p>
    </div>
    <ul class="contacts">
      <li class="contacts__item contacts__item--address">
        <span>4128 Linden Avenue<br>Hartford, CT 06105</span>
        <svg class="contacts__icon" viewBox="0 0 16 16"><path d="M8 1a5 5 0 0 0-5 5c0 3.5 5 9 5 9s5-5.5 5-9a5 5 0 0 0-5-5zm0 7a2 2 0 1 1 0-4 2 2 0 0 1 0 4z"/></svg>
      </li>
      <li class="contacts__item">
        <span>(555) 014-2368</span>
        <svg class="contacts__icon" viewBox="0 0 16 16"><path d="M4 1l3 3-2 2c1 2 3 4 5 5l2-2 3 3-2 2C7 14 2 9 2 3z"/></svg>
      </li>
      <li class="contacts__item">
        <span>(555) 014-2369</span>
        <svg class="contacts__icon" viewBox="0 0 16 16"><path d="M4 1h8v14H4zM5.5 2.5v9h5v-9zM7 12.5h2v1H7z"/></svg>
      </li>
      <li class="contacts__item">
        <span>(555) 014-2370</span>
        <svg class="contacts__icon" viewBox="0 0 16 16"><path d="M4 1h8v4H4zM1 6h14v6h-2v3H3v-3H1zm3 4v3.5h8V10z"/></svg>
      </li>
      <li class="contacts__item">
        <span>hello@velorahealth.com</span>
        <svg class="contacts__icon" viewBox="0 0 16 16"><path d="M1 3h14v1.5L8 9 1 4.5zM1 6.5 8 11l7-4.5V13H1z"/></svg>
      </li>
      <li class="contacts__item">
        <span>velorahealth.com</span>
        <svg class="contacts__icon" viewBox="0 0 16 16"><circle cx="8" cy="8" r="7"/></svg>
      </li>
    </ul>
  </section>

  <section class="card card--back" aria-label="Business card back">
    <div class="brand">
      <span class="brand__mark"></span>
      <span class="brand__name">Velora Health</span>
    </div>
  </section>
</main>
</body>
</html>
```